Design for online reviews widget

Attached is a wireframe of a widget we need designing to display reviews on websites from multiple sources. We need this provided at 3 different sizes including full screen, contained (like the wireframe) and mobile.
You have completely free rein on the styling.
The only elements that should remain untouched are the blue stars (https://www.filquarry.net/s/8vtmwp2291zq4h/kv%20stars.ai?dl=0) and powered by logo at the bottom.
Ignore the menu at the top of the wireframe, this is just from the website the widget will be placed on.
Businesses

```html
<!DOCTYPE html>
<html lang="en">
<head>
<meta charset="utf-8">
<title>Review Widget – Dark and Light</title>
<link rel="stylesheet" href="https://fonts.googleapis.com/css2?family=Exo+2:wght@400;500;600;700&family=Roboto:ital,wght@0,400;1,400&display=swap">
<style>
  :root {
    --page: #ffffff;
    --sky: #36b3e8;
    --tile: #eaf6fc;
    --tile-text: #222222;
    --green: #3ecf4a;
    --verified: #36c94a;
    --gold: #f6b51e;
    --yellow: #f9cf2a;
    --teal: #1fa86a;
    --dark-panel: #2a2a2a;
    --dark-card: #363636;
    --dark-title: #ffffff;
    --dark-body: #cfcfcf;
    --light-panel: #ffffff;
    --light-card: #ffffff;
    --light-title: #222222;
    --light-body: #6c6c6c;
  }
  * { box-sizing: border-box; margin: 0; padding: 0; }
  html, body { width: 1200px; height: 958px; overflow: hidden; background: var(--page); }
  body { position: relative; font-family: "Exo 2", sans-serif; }

  .widget { position: absolute; top: 31px; width: 548px; height: 896px; }
  .widget--dark {
    left: 34px; background: var(--dark-panel);
    --card: var(--dark-card); --title: var(--dark-title); --body: var(--dark-body);
    --select-bg: #2a2a2a; --select-text: #ddd; --select-line: #666;
  }
  .widget--light {
    left: 622px; background: var(--light-panel);
    box-shadow: 0 0 6px rgba(0,0,0,0.12);
    --card: var(--light-card); --title: var(--light-title); --body: var(--light-body);
    --select-bg: #fff; --select-text: #555; --select-line: #bbb;
  }

  .score-stars { position: absolute; top: 27px; left: 0; width: 100%; display: flex; justify-content: center; gap: 3px; }
  .score-stars svg { width: 20px; height: 20px; }
  .score-caption { position: absolute; top: 51px; width: 100%; text-align: center; font-family: "Roboto", sans-serif; font-style: italic; font-size: 5.6px; color: var(--body); }

  .filter {
    position: absolute; left: 417px; top: 65px; width: 62px; height: 14px;
    background: var(--select-bg); border: 0.6px solid var(--select-line);
    font-family: "Roboto", sans-serif; font-size: 4.5px; color: var(--select-text);
    padding: 4px 0 0 4px;
  }
  .filter::after { content: "▾"; position: absolute; right: 4px; top: 3.5px; font-size: 5px; }

  .review { position: absolute; left: 70px; width: 409px; height: 160px; background: var(--card); }
  .widget--light .review { box-shadow: 0 1px 5px rgba(0,0,0,0.13); }

  .source-tile { position: absolute; left: 17px; top: 17px; width: 100px; height: 126px; background: var(--tile); }
  .source-name {
    position: absolute; left: 0; width: 100%; text-align: center;
    font-weight: 600; font-size: 15px; color: var(--tile-text); white-space: nowrap;
  }
  .score-disc {
    position: absolute; left: 15px; top: 38px; width: 70px; height: 70px; border-radius: 50%;
    background: var(--sky); color: #fff; font-size: 19px; font-weight: 600;
    display: flex; align-items: center; justify-content: center;
  }
  .rating-strip { position: absolute; background: #fff; display: flex; justify-content: center; align-items: center; gap: 1px; }
  .rating-strip svg { width: 14px; height: 14px; }

  .review-body { position: absolute; left: 135px; top: 24px; width: 256px; }
  .review-title { font-size: 10.5px; font-weight: 400; color: var(--title); line-height: 14px; white-space: nowrap; }
  .review-text {
    margin-top: 6px; font-family: "Roboto", sans-serif; font-style: italic; font-size: 5.9px;
    line-height: 9.2px; color: var(--body);
  }
  .metrics { position: absolute; top: 92px; display: flex; }
  .metric { font-size: 6.5px; font-weight: 400; color: var(--title); }
  .metric b { display: block; font-weight: 500; font-size: 11px; color: var(--sky); margin-top: 1px; }
  .service { position: absolute; top: 92px; font-size: 6.5px; font-weight: 400; color: var(--title); }
  .service b { display: block; font-weight: 500; font-size: 11px; color: var(--sky); margin-top: 1px; }
  .review-meta { position: absolute; left: 135px; top: 129px; font-size: 5px; color: var(--verified); }

  .load-more {
    position: absolute; left: 70px; top: 782px; width: 80px; height: 22px; background: var(--green);
    color: #fff; font-size: 7px; display: flex; align-items: center; justify-content: center;
  }

  .powered { position: absolute; left: 372px; top: 840px; width: 160px; }
  .powered-label { position: absolute; left: 35px; top: 0; font-size: 10px; color: var(--title); }
  .powered-mark { position: absolute; left: 2px; top: 16px; width: 24px; height: 24px; border-radius: 50%; background: var(--sky); }
  .powered-name { position: absolute; left: 33px; top: 13px; font-size: 16px; font-weight: 700; color: var(--title); }
</style>
</head>
<body>
<svg width="0" height="0" style="position:absolute">
  <defs>
    <symbol id="star" viewBox="0 0 24 24"><path d="M12 2.5l2.9 6.1 6.6.8-4.9 4.6 1.3 6.6L12 17.3l-5.9 3.3 1.3-6.6-4.9-4.6 6.6-.8z"/></symbol>
    <symbol id="badge-star" viewBox="0 0 40 40"><circle cx="20" cy="20" r="20" fill="#36b3e8"/><path fill="#fff" d="M20 7.5l3.6 7.6 8.3 1-6.1 5.7 1.6 8.2L20 26l-7.4 4 1.6-8.2-6.1-5.7 8.3-1z"/></symbol>
  </defs>
</svg>

<!-- Dark theme -->
<section class="widget widget--dark">
  <div class="score-stars" aria-label="4.3 out of 5">
    <svg><use href="#badge-star"/></svg><svg><use href="#badge-star"/></svg><svg><use href="#badge-star"/></svg><svg><use href="#badge-star"/></svg><svg><use href="#badge-star"/></svg>
  </div>
  <p class="score-caption">Combined Review Score 4.3 out of 5</p>
  <div class="filter">Filter result</div>

  <article class="review" style="top:84px">
    <div class="source-tile">
      <span class="source-name" style="top:10px">CraftVerify</span>
      <div class="score-disc">9.77</div>
    </div>
    <div class="review-body">
      <h2 class="review-title">Front door with windows each side and side window</h2>
      <p class="review-text">"This is the second time we have used kestrel home Improvements , and the service is amazing! Owen came round several times as we keep changing our minds and he was so helpful and gave us good advice, and the guys who do the fitting are efficient and tidy . I've got to say the end result is amazing and I have recommended to many of friends . Thanks Kestrel"</p>
    </div>
    <div class="metrics" style="left:135px">
      <div class="metric" style="width:49px">Reliability:<b>9.38</b></div>
      <div class="metric" style="width:46px">Courtesy:<b>10</b></div>
      <div class="metric" style="width:44px">Tidiness:<b>9.84</b></div>
      <div class="metric">Workmanship<b>10</b></div>
    </div>
    <p class="review-meta">Verified 28th September 2021 | Located in Ashford Vale</p>
  </article>

  <article class="review" style="top:259px">
    <div class="source-tile">
      <span class="source-name" style="top:32px">Searchly</span>
      <div class="rating-strip" style="left:10px;top:71px;width:80px;height:23px;fill:var(--gold)">
        <svg><use href="#star"/></svg><svg><use href="#star"/></svg><svg><use href="#star"/></svg><svg><use href="#star"/></svg><svg><use href="#star"/></svg>
      </div>
    </div>
    <div class="review-body">
      <h2 class="review-title">Positive: Professionalism, Quality, Value</h2>
      <p class="review-text">"The team did a good job of replacing a large feature window spanning two floors, as well as the others in my property. They're a professional group who were willing to work out solutions to any problem, especially compared to other companies. Prices are fair, and my new UPVC windows look great. Special thanks to Frank for being so accommodating and for the good communication throughout"</p>
    </div>
    <div class="service" style="left:135px">Service:<b>Window installation</b></div>
    <p class="review-meta">Verified 28th September 2021 | Located in Ashford Vale</p>
  </article>

  <article class="review" style="top:434px">
    <div class="source-tile">
      <span class="source-name" style="top:34px">Dialbook</span>
      <div class="rating-strip" style="left:8px;top:68px;width:85px;height:24px;fill:var(--yellow)">
        <svg style="width:15px;height:15px"><use href="#star"/></svg><svg style="width:15px;height:15px"><use href="#star"/></svg><svg style="width:15px;height:15px"><use href="#star"/></svg><svg style="width:15px;height:15px"><use href="#star"/></svg><svg style="width:15px;height:15px"><use href="#star"/></svg>
      </div>
    </div>
    <div class="review-body">
      <h2 class="review-title">Brilliant all round professional, friendly service.</h2>
      <p class="review-text">"This home run friendly business was a real pleasure to deal with. From the professional, no pressure quote, nothing was too much trouble to ensure everything is as required for your needs with the quote and fitting. The workmanship and double glazing being fitted was brilliant and my home/outdoors was left tidy and clean leaving an outstanding impression for such an all round professional job. I would not hesitate to recommend this company, such a brilliant service from great hardworking people that care about their service."</p>
    </div>
    <p class="review-meta">13 Feb 2018 by GreenChair41</p>
  </article>

  <article class="review" style="top:609px">
    <div class="source-tile">
      <span class="source-name" style="top:36px">Ratewell</span>
      <div class="rating-strip" style="left:10px;top:68px;width:80px;height:26px;fill:var(--teal)">
        <svg><use href="#star"/></svg><svg><use href="#star"/></svg><svg><use href="#star"/></svg><svg><use href="#star"/></svg><svg><use href="#star"/></svg>
      </div>
    </div>
    <div class="review-body">
      <h2 class="review-title">Front door with windows each side and side window</h2>
      <p class="review-text">This is the second time we have used kestrel home Improvments , and the service is amazing! Owen came round several times as we keep changing our minds and he was so helpful and gave us good advice, and the guys who do the fitting are efficient and tidy . I've got to say the end result is amazing and I have recommended to many of friends . Thanks Kestrel</p>
    </div>
    <p class="review-meta">13 Feb 2018 by Tom</p>
  </article>

  <div class="load-more">Load more</div>
  <div class="powered">
    <span class="powered-label">Powered by</span>
    <span class="powered-mark"></span>
    <span class="powered-name">StarTally</span>
  </div>
</section>

<!-- Light theme -->
<section class="widget widget--light">
  <div class="score-stars" aria-label="4.3 out of 5">
    <svg><use href="#badge-star"/></svg><svg><use href="#badge-star"/></svg><svg><use href="#badge-star"/></svg><svg><use href="#badge-star"/></svg><svg><use href="#badge-star"/></svg>
  </div>
  <p class="score-caption">Combined Review Score 4.3 out of 5</p>
  <div class="filter">Filter result</div>

  <article class="review" style="top:84px">
    <div class="source-tile">
      <span class="source-name" style="top:10px">CraftVerify</span>
      <div class="score-disc">9.77</div>
    </div>
    <div class="review-body">
      <h2 class="review-title">Front door with windows each side and side window</h2>
      <p class="review-text">"This is the second time we have used kestrel home Improvements , and the service is amazing! Owen came round several times as we keep changing our minds and he was so helpful and gave us good advice, and the guys who do the fitting are efficient and tidy . I've got to say the end result is amazing and I have recommended to many of friends . Thanks Kestrel"</p>
    </div>
    <div class="metrics" style="left:135px">
      <div class="metric" style="width:49px">Reliability:<b>9.38</b></div>
      <div class="metric" style="width:46px">Courtesy:<b>10</b></div>
      <div class="metric" style="width:44px">Tidiness:<b>9.84</b></div>
      <div class="metric">Workmanship<b>10</b></div>
    </div>
    <p class="review-meta">Verified 28th September 2021 | Located in Ashford Vale</p>
  </article>

  <article class="review" style="top:259px">
    <div class="source-tile">
      <span class="source-name" style="top:32px">Searchly</span>
      <div class="rating-strip" style="left:10px;top:71px;width:80px;height:23px;fill:var(--gold)">
        <svg><use href="#star"/></svg><svg><use href="#star"/></svg><svg><use href="#star"/></svg><svg><use href="#star"/></svg><svg><use href="#star"/></svg>
      </div>
    </div>
    <div class="review-body">
      <h2 class="review-title">Positive: Professionalism, Quality, Value</h2>
      <p class="review-text">"The team did a good job of replacing a large feature window spanning two floors, as well as the others in my property. They're a professional group who were willing to work out solutions to any problem, especially compared to other companies. Prices are fair, and my new UPVC windows look great. Special thanks to Frank for being so accommodating and for the good communication throughout"</p>
    </div>
    <div class="service" style="left:135px">Service:<b>Window installation</b></div>
    <p class="review-meta">Verified 28th September 2021 | Located in Ashford Vale</p>
  </article>

  <article class="review" style="top:434px">
    <div class="source-tile">
      <span class="source-name" style="top:34px">Dialbook</span>
      <div class="rating-strip" style="left:8px;top:68px;width:85px;height:24px;fill:var(--yellow)">
        <svg style="width:15px;height:15px"><use href="#star"/></svg><svg style="width:15px;height:15px"><use href="#star"/></svg><svg style="width:15px;height:15px"><use href="#star"/></svg><svg style="width:15px;height:15px"><use href="#star"/></svg><svg style="width:15px;height:15px"><use href="#star"/></svg>
      </div>
    </div>
    <div class="review-body">
      <h2 class="review-title">Brilliant all round professional, friendly service.</h2>
      <p class="review-text">"This home run friendly business was a real pleasure to deal with. From the professional, no pressure quote, nothing was too much trouble to ensure everything is as required for your needs with the quote and fitting. The workmanship and double glazing being fitted was brilliant and my home/outdoors was left tidy and clean leaving an outstanding impression for such an all round professional job. I would not hesitate to recommend this company, such a brilliant service from great hardworking people that care about their service."</p>
    </div>
  </article>

  <article class="review" style="top:609px">
    <div class="source-tile">
      <span class="source-name" style="top:36px">Ratewell</span>
      <div class="rating-strip" style="left:10px;top:68px;width:80px;height:26px;fill:var(--teal)">
        <svg><use href="#star"/></svg><svg><use href="#star"/></svg><svg><use href="#star"/></svg><svg><use href="#star"/></svg><svg><use href="#star"/></svg>
      </div>
    </div>
    <div class="review-body">
      <h2 class="review-title">Front door with windows each side and side window</h2>
      <p class="review-text">This is the second time we have used kestrel home Improvments , and the service is amazing! Owen came round several times as we keep changing our minds and he was so helpful and gave us good advice, and the guys who do the fitting are efficient and tidy . I've got to say the end result is amazing and I have recommended to many of friends . Thanks Kestrel</p>
    </div>
    <p class="review-meta">13 Feb 2018 by Tom</p>
  </article>

  <div class="load-more">Load more</div>
  <div class="powered">
    <span class="powered-label">Powered by</span>
    <span class="powered-mark"></span>
    <span class="powered-name">StarTally</span>
  </div>
</section>
</body>
</html>
```